Accountability Project Graphics

I want to create 10 social media graphics (new Instagram size 4:5 (1080 x 1350 pixels) focusing on our Kelmora Accountability App, using any of the 3 pictures attached. Use the attached pics only, NO RANDOM STOCK PHOTOGRAPHY. For the color scheme, use the landing page colors/fonts (attached).
You can add any of the 3 photos attached but I mainly need BOLD text that includes these headlines and sub-headlines on them.
Please NOTE for all the headlines below, also add this sub-headline on each graphic:
Stay Consistent with MB in Your Pocket!
Here are the headlines:
• Stop Starting Over Every Monday
• You don't need more willpower. You need more support
• Built for women who are tired of doing this alone
• When Motivation Fades, MB Checks In
• The Support System You've Been Missing
• Support When Motivation Disappears
• What if MB Checked in Every Day?
• The Missing Piece Isn't Another Diet
• Eat the food you love. Stay accountable every day.
• One Bad Meal Doesn't Mean You Failed
women over 40 trying to lose weight

```html
<!DOCTYPE html>
<html lang="en">
<head>
<meta charset="utf-8">
<title>Kelmora Accountability Social Set</title>
<link href="https://fonts.googleapis.com/css2?family=Merriweather:ital,wght@0,900;1,900&family=Lexend:wght@400;500&display=swap" rel="stylesheet">
<style>
:root{
  --board:#ebc2d0;
  --card:#f8dde7;
  --card-deep:#eeb3c8;
  --ink:#2a1326;
  --accent:#c24b7c;
  --line:#d88aa7;
  --white:#ffffff;
  --photo-a:#3a2a3a;
  --photo-b:#c9a0b4;
}
*{margin:0;padding:0;box-sizing:border-box}
html,body{width:1200px;height:606px;overflow:hidden;background:var(--board)}
.board{position:relative;width:1200px;height:606px}
.post{position:absolute;width:207px;height:259px;overflow:hidden;
  background:linear-gradient(160deg,var(--card) 55%,var(--card-deep));
  box-shadow:0 4px 10px rgba(120,40,70,.22)}
.photo{position:absolute}
.photo--portrait{background:linear-gradient(180deg,var(--photo-b) 0%,var(--photo-a) 38%,#1f1a26 100%)}
.photo--duo{background:linear-gradient(160deg,#e9b8ca 0%,#6a5a74 40%,#2f3e5a 100%)}
.photo--hug{background:linear-gradient(160deg,#e8a7c2 0%,#7a4a5e 40%,#d9e8b6 100%)}
.headline{position:absolute;font-family:"Merriweather",serif;font-weight:900;color:var(--ink);line-height:1.02;letter-spacing:-.2px}
.headline em{color:var(--accent);font-style:italic}
.headline--center{text-align:center}
.tag{position:absolute;font-family:"Lexend",sans-serif;font-size:3.6px;font-weight:500;color:var(--accent);
  background:var(--white);border:.5px solid var(--line);border-radius:6px;padding:1.5px 5px;letter-spacing:.2px;white-space:nowrap}
.subline{position:absolute;font-family:"Lexend",sans-serif;font-size:7px;font-weight:500;color:var(--ink);line-height:1.3;
  background:rgba(255,255,255,.55);border:.6px solid var(--line);border-radius:7px;padding:6px 7px}
.subline--plain{background:none;border:none;padding:0;text-align:center}
.divider{position:absolute;height:8px}
.divider::before{content:"";position:absolute;left:0;right:0;top:4px;border-top:.6px solid var(--line)}
.divider svg{position:absolute;left:50%;top:0;transform:translateX(-50%);background:var(--card)}
.panel{position:absolute;border-radius:50%;background:rgba(255,255,255,.45)}
</style>
</head>
<body>
<main class="board">

  <!-- 1 -->
  <section class="post" style="left:30px;top:30px">
    <div class="photo photo--portrait" role="img" aria-label="Smiling coach in black outfit, hand on hip" style="left:105px;top:0;width:102px;height:259px"></div>
    <span class="tag" style="left:8px;top:15px">KELMORA · MB IN YOUR POCKET</span>
    <h2 class="headline" style="left:9px;top:28px;font-size:21px">Stop<br>Starting<br>Over<br><em>Every<br>Monday</em></h2>
    <div class="divider" style="left:8px;top:143px;width:95px"><svg width="10" height="8" viewBox="0 0 10 8"><path d="M5 8 1 4a2 2 0 0 1 4-3 2 2 0 0 1 4 3z" fill="var(--accent)"/></svg></div>
    <p class="subline" style="left:6px;top:160px;width:92px">Stay Consistent with<br>MB in Your Pocket!</p>
  </section>

  <!-- 2 -->
  <section class="post" style="left:264px;top:30px">
    <div class="photo photo--portrait" role="img" aria-label="Smiling coach in black outfit" style="left:0;top:0;width:96px;height:259px"></div>
    <span class="tag" style="left:98px;top:34px">KELMORA · MB IN YOUR POCKET</span>
    <h2 class="headline" style="left:98px;top:48px;font-size:16.5px;line-height:1.16">You Don't<br>Need More<br><em>Willpower</em><br>You Need<br>More<br><em>Support</em></h2>
    <div class="divider" style="left:98px;top:170px;width:78px"><svg width="10" height="8" viewBox="0 0 10 8"><path d="M5 8 1 4a2 2 0 0 1 4-3 2 2 0 0 1 4 3z" fill="var(--accent)"/></svg></div>
    <p class="subline" style="left:96px;top:182px;width:92px;background:var(--white)">Stay Consistent with<br>MB in Your Pocket!</p>
  </section>

  <!-- 3 -->
  <section class="post" style="left:492px;top:30px">
    <div class="photo photo--hug" role="img" aria-label="Two women hugging and laughing" style="left:0;top:95px;width:207px;height:164px"></div>
    <span class="tag" style="left:70px;top:8px">KELMORA · MB IN YOUR POCKET</span>
    <h2 class="headline headline--center" style="left:0;width:207px;top:21px;font-size:16px">Built For<br>Women Who Are<br>Tired Of <em>Doing<br>This Alone</em></h2>
    <p class="subline" style="left:133px;top:90px;width:72px;font-size:5.5px;padding:5px;background:var(--white)">Stay Consistent with<br>MB in Your Pocket!</p>
  </section>

  <!-- 4 -->
  <section class="post" style="left:728px;top:30px">
    <div class="photo photo--duo" role="img" aria-label="Two women laughing side by side" style="left:0;top:100px;width:207px;height:159px"></div>
    <span class="tag" style="left:15px;top:9px">KELMORA · MB IN YOUR POCKET</span>
    <h2 class="headline" style="left:17px;top:25px;font-size:17.5px">When<br><em>Motivation</em><br>Fades, <em>MB<br>Checks In</em></h2>
    <p class="subline" style="left:125px;top:66px;width:84px;font-size:6.5px;background:var(--white)">Stay Consistent with<br>MB in Your Pocket!</p>
  </section>

  <!-- 5 -->
  <section class="post" style="left:962px;top:30px">
    <div class="photo photo--portrait" role="img" aria-label="Smiling coach in black outfit, hand on hip" style="left:120px;top:55px;width:87px;height:204px"></div>
    <span class="tag" style="left:10px;top:22px">KELMORA · MB IN YOUR POCKET</span>
    <h2 class="headline" style="left:11px;top:42px;font-size:18px">The <em>Support</em><br>System<br>You've Been<br><em>Missing</em></h2>
    <div class="divider" style="left:12px;top:141px;width:105px"><svg width="10" height="8" viewBox="0 0 10 8"><path d="M5 8 1 4a2 2 0 0 1 4-3 2 2 0 0 1 4 3z" fill="var(--accent)"/></svg></div>
    <p class="subline" style="left:9px;top:161px;width:102px">Stay Consistent with<br>MB in Your Pocket!</p>
  </section>

  <!-- 6 -->
  <section class="post" style="left:30px;top:316px">
    <div class="photo photo--portrait" role="img" aria-label="Smiling coach in black outfit, hand on hip" style="left:135px;top:8px;width:72px;height:251px"></div>
    <span class="tag" style="left:13px;top:50px">KELMORA · MB IN YOUR POCKET</span>
    <h2 class="headline" style="left:13px;top:66px;font-size:19px">Support<br>When<br>Motivation<br><em>Disappears</em></h2>
    <div class="divider" style="left:40px;top:161px;width:40px"><svg width="10" height="8" viewBox="0 0 10 8"><path d="M5 8 1 4a2 2 0 0 1 4-3 2 2 0 0 1 4 3z" fill="var(--accent)"/></svg></div>
    <p class="subline" style="left:12px;top:167px;width:102px">Stay Consistent with<br>MB in Your Pocket!</p>
  </section>

  <!-- 7 -->
  <section class="post" style="left:264px;top:316px">
    <div class="photo photo--hug" role="img" aria-label="Two women hugging and laughing" style="left:55px;top:80px;width:152px;height:179px"></div>
    <span class="tag" style="left:15px;top:15px">KELMORA · MB IN YOUR POCKET</span>
    <p class="subline" style="left:115px;top:13px;width:94px;font-size:7px">Stay Consistent with<br>MB in Your Pocket!</p>
    <h2 class="headline" style="left:16px;top:31px;font-size:19px;line-height:1.1">What if<br>MB <em>Checked<br>in</em> Every<br>Day?</h2>
  </section>

  <!-- 8 -->
  <section class="post" style="left:492px;top:316px">
    <div class="photo photo--duo" role="img" aria-label="Two women laughing side by side" style="left:10px;top:105px;width:197px;height:154px"></div>
    <span class="tag" style="left:65px;top:12px">KELMORA · MB IN YOUR POCKET</span>
    <h2 class="headline headline--center" style="left:0;width:207px;top:24px;font-size:20.5px">The Missing<br>Piece Isn't<br><em>Another Diet</em></h2>
    <p class="subline" style="left:11px;top:92px;width:102px">Stay Consistent with<br>MB in Your Pocket!</p>
  </section>

  <!-- 9 -->
  <section class="post" style="left:728px;top:316px">
    <div class="photo photo--portrait" role="img" aria-label="Smiling coach in black outfit" style="left:0;top:0;width:90px;height:259px"></div>
    <div class="panel" style="left:72px;top:20px;width:200px;height:210px"></div>
    <span class="tag" style="left:100px;top:40px">KELMORA · MB IN YOUR POCKET</span>
    <h2 class="headline headline--center" style="left:78px;width:112px;top:54px;font-size:15px;line-height:1.28">Eat The<br>Food <em>You<br>Love</em> Stay<br>Accountable<br><em>Every Day.</em></h2>
    <div class="divider" style="left:90px;top:159px;width:92px"><svg width="10" height="8" viewBox="0 0 10 8"><path d="M5 8 1 4a2 2 0 0 1 4-3 2 2 0 0 1 4 3z" fill="var(--accent)"/></svg></div>
    <p class="subline subline--plain" style="left:80px;width:112px;top:174px">Stay Consistent with<br>MB in Your Pocket!</p>
  </section>

  <!-- 10 -->
  <section class="post" style="left:962px;top:316px">
    <div class="photo photo--portrait" role="img" aria-label="Smiling coach in black outfit, hand on hip" style="left:110px;top:50px;width:97px;height:209px"></div>
    <span class="tag" style="left:14px;top:17px">KELMORA · MB IN YOUR POCKET</span>
    <h2 class="headline" style="left:15px;top:30px;font-size:17px;line-height:1.2">One Bad<br>Meal Doesn't<br>Mean <em>You<br>Failed</em></h2>
    <p class="subline" style="left:12px;top:118px;width:102px">Stay Consistent with<br>MB in Your Pocket!</p>
  </section>

</main>
</body>
</html>
```